Online-Marketing Material für Onlineshop für nachhaltiges Hundezubehör
Zielgruppe
Wir sind ein onlineshop für nachhaltiges Hundezubehör und sind auf der Suche nach einem Banner für unsere Startseite
Aufgabenstellung
wir bieten viele produkte an die aus upgecycelten kletterseilen hergestellt werden(Hundeleinen, Halsbänder, Spielzeug)
das banner soll die nachhaltigkeit unseres hundeshops hervorheben und vertrauen beim kunden generieren.
Vielleicht auch etwas wo der Positive Aspekt des upcyclings auf unsere Erde(weniger Plastik) hervorgehoben wird.
Auf jeden Fall muss(mindestens) ein Hund auf dem Banner zu sehen sein und man muss den Bezug zu Nachhaltigkeit herstellen könen.
Was slogans angeht sind euch natürlich auch keine grenzen gesetzt, umso kreativer, umso besser :)
Das Banner brauche ich in den Maßen 1920x500 , 1280x1000 und 1280x2000

```html
<!DOCTYPE html>
<html lang="de">
<head>
<meta charset="utf-8">
<title>Jeder kann sein Ein Held der Erde – Bannerformate</title>
<link rel="stylesheet" href="https://fonts.googleapis.com/css2?family=Source+Sans+3:wght@400;600;700&display=swap">
<style>
  :root {
    --navy: #15324f;
    --green: #6a9a26;
    --text: #1f2a3a;
    --paper: #ffffff;
    --sky-top: #b9c2c8;
    --sky-light: #e4e6e5;
    --hill-light: #7c9b55;
    --hill-mid: #4f7a33;
    --hill-dark: #355a24;
    --dog-tan: #c98a45;
    --dog-dark: #3a2a20;
    --cape: #d9283a;
  }
  * { box-sizing: border-box; margin: 0; padding: 0; }
  html, body { width: 938px; height: 1200px; overflow: hidden; background: var(--paper); }
  body { position: relative; font-family: "Source Sans 3", "Source Sans Pro", sans-serif; color: var(--text); }

  .banner {
    position: absolute;
    background: var(--paper);
    overflow: hidden;
    box-shadow: 0 2px 10px rgba(0,0,0,0.10);
  }
  .banner--square { left: 47px; top: 140px; width: 410px; height: 319px; }
  .banner--tall   { left: 483px; top: 140px; width: 410px; height: 638px; }
  .banner--wide   { left: 47px; top: 838px; width: 846px; height: 219px; }

  .landscape { position: absolute; left: 0; top: 0; width: 100%; height: 100%; }

  .headline {
    position: absolute;
    font-weight: 700;
    line-height: 1.05;
    letter-spacing: 0.2px;
  }
  .headline span { display: block; }
  .headline .lead { color: var(--navy); }
  .headline .hero { color: var(--green); }

  .product-set {
    position: absolute;
    border-radius: 6px 6px 14px 14px;
    background: linear-gradient(90deg, #b78a58 0%, #c59a6a 35%, #e3b3ad 60%, #d9a583 80%, #8fb1d4 100%);
    opacity: 0.92;
  }
  .dog {
    position: absolute;
    border-radius: 45% 45% 30% 30% / 30% 30% 20% 20%;
    background: linear-gradient(180deg, var(--dog-dark) 0%, #5a3a26 30%, var(--cape) 55%, var(--dog-tan) 85%, #b87a3a 100%);
  }

  .hashtag { position: absolute; font-weight: 700; color: var(--navy); white-space: nowrap; }
  .hashtag em { font-style: normal; color: var(--green); }
  .copy { position: absolute; font-weight: 400; color: var(--text); hyphens: auto; }
  .copy em { font-style: normal; color: var(--green); }

  /* square */
  .banner--square .headline { left: 0; width: 100%; top: 16px; text-align: center; font-size: 25px; }
  .banner--square .product-set { left: 25px; top: 142px; width: 132px; height: 84px; }
  .banner--square .dog { left: 303px; top: 153px; width: 85px; height: 156px; }
  .banner--square .hashtag { left: 26px; top: 239px; font-size: 13px; }
  .banner--square .copy { left: 28px; top: 258px; width: 270px; font-size: 8.4px; line-height: 14.6px; font-weight: 600; }

  /* tall */
  .banner--tall .headline { left: 0; width: 100%; top: 42px; text-align: center; font-size: 35px; line-height: 40px; }
  .banner--tall .product-set { left: 44px; top: 360px; width: 154px; height: 106px; }
  .banner--tall .dog { left: 270px; top: 400px; width: 127px; height: 228px; }
  .banner--tall .hashtag { left: 26px; top: 486px; font-size: 17.5px; }
  .banner--tall .copy { left: 28px; top: 521px; width: 236px; font-size: 12.5px; line-height: 16.5px; }

  /* wide */
  .banner--wide .headline { left: 34px; top: 18px; font-size: 30px; line-height: 33px; }
  .banner--wide .product-set { left: 107px; top: 117px; width: 138px; height: 90px; }
  .banner--wide .dog { left: 378px; top: 32px; width: 102px; height: 183px; }
  .banner--wide .hashtag { left: 556px; top: 37px; font-size: 17.5px; }
  .banner--wide .copy { left: 560px; top: 70px; width: 255px; font-size: 14.6px; line-height: 21.5px; }
</style>
</head>
<body>

<svg width="0" height="0" style="position:absolute">
  <defs>
    <linearGradient id="hills" x1="0" y1="0" x2="0" y2="1">
      <stop offset="0" stop-color="#b9c2c8"/>
      <stop offset="0.28" stop-color="#e4e6e5"/>
      <stop offset="0.40" stop-color="#a9b6b3"/>
      <stop offset="0.48" stop-color="#7c9b55"/>
      <stop offset="0.75" stop-color="#4f7a33"/>
      <stop offset="1" stop-color="#355a24"/>
    </linearGradient>
    <linearGradient id="hills-tall" x1="0" y1="0" x2="0" y2="1">
      <stop offset="0" stop-color="#b9c2c8"/>
      <stop offset="0.16" stop-color="#e4e6e5"/>
      <stop offset="0.30" stop-color="#a9b6b3"/>
      <stop offset="0.38" stop-color="#7c9b55"/>
      <stop offset="0.70" stop-color="#4f7a33"/>
      <stop offset="1" stop-color="#3d6628"/>
    </linearGradient>
  </defs>
</svg>

<section class="banner banner--square">
  <svg class="landscape" viewBox="0 0 410 319" preserveAspectRatio="none" role="img" aria-label="Foto: grüne Hügellandschaft mit Windrädern unter bewölktem Himmel">
    <path fill="url(#hills)" d="M0 0 H410 V212 C385 222 360 258 335 236 C308 208 275 224 232 236 C182 248 122 226 82 212 C50 201 22 196 0 200 Z"/>
  </svg>
  <h1 class="headline"><span class="lead">Jeder kann sein</span><span class="hero">Ein Held der Erde</span></h1>
  <div class="product-set" role="img" aria-label="Produktfoto: Kotbeutelbox, Snacktüte, Seilleine und Halsband"></div>
  <div class="dog" role="img" aria-label="Foto: Welpe mit rotem Umhang blickt nach oben"></div>
  <p class="hashtag">#JoinOur<em>GreenMovement</em></p>
  <p class="copy">Unserer Produkte darauf, dass durch <em>Upcycling</em> und <em>Recycling</em> so wenig neues Plastik entsteht wie möglich!. Unsere Produkte sind außerdem vegan und frei von Tierleid.</p>
</section>

<section class="banner banner--tall">
  <svg class="landscape" viewBox="0 0 410 638" preserveAspectRatio="none" role="img" aria-label="Foto: grüne Hügellandschaft mit Windrädern unter bewölktem Himmel">
    <path fill="url(#hills-tall)" d="M0 0 H410 V450 C390 460 372 500 345 478 C320 456 300 462 260 462 C210 462 150 454 100 430 C60 414 28 410 0 418 Z"/>
  </svg>
  <h2 class="headline"><span class="lead">Jeder kann sein</span><span class="hero">Ein Held der Erde</span></h2>
  <div class="product-set" role="img" aria-label="Produktfoto: Kotbeutelbox, Snacktüte, Seilleine und Halsband"></div>
  <div class="dog" role="img" aria-label="Foto: Welpe mit rotem Umhang blickt nach oben"></div>
  <p class="hashtag">#JoinOur<em>GreenMovement</em></p>
  <p class="copy">Unserer Produkte darauf, dass durch <em>Upcycling</em> und <em>Recycling</em> so wenig neues Plastik entsteht wie möglich!. Unsere Produkte sind außerdem vegan und frei von Tierleid.</p>
</section>

<section class="banner banner--wide">
  <svg class="landscape" viewBox="0 0 846 219" preserveAspectRatio="none" role="img" aria-label="Foto: grüne Hügellandschaft mit Windrädern unter bewölktem Himmel">
    <path fill="url(#hills)" d="M0 0 H530 C514 22 520 62 526 92 C532 132 502 150 470 160 C420 176 380 200 330 202 C262 204 200 188 140 176 C82 165 32 150 0 118 Z"/>
  </svg>
  <h2 class="headline"><span class="lead">Jeder kann sein</span><span class="hero">Ein Held der Erde</span></h2>
  <div class="product-set" role="img" aria-label="Produktfoto: Kotbeutelbox, Snacktüte, Seilleine und Halsband"></div>
  <div class="dog" role="img" aria-label="Foto: Welpe mit rotem Umhang blickt nach oben"></div>
  <p class="hashtag">#JoinOur<em>GreenMovement</em></p>
  <p class="copy">Unserer Produkte darauf, dass durch <em>Upcycling</em> und <em>Recycling</em> so wenig neues Plastik entsteht wie möglich!. Unsere Produkte sind außerdem vegan und frei von Tierleid.</p>
</section>

</body>
</html>
```